Real Estate Design Website

I would like to have a design for "real estate agent" website. It needs to be in a "Responsive" framework.

The design need to be suitable for different viewer from all around the world. It needs to be modern. It'd be great if there is a design for mobile and vexo/tablet (it's all under responsive framework). It needs to be easy to navigate and look modern

Target Market(s)

End user/Real estate buyers from different part of the world

Industry/Entity Type

Real Estate

Requirements
Must have
• It's for real estate agent website which is used to represent their brand/image but at the same time it also for their client which is real estate buyers
Should not have
• Should not be boring design/out of date

```html
<!DOCTYPE html>
<html lang="en">
<head>
<meta charset="utf-8">
<title>Brightlot – responsive home screens</title>
<link rel="stylesheet" href="https://fonts.googleapis.com/css2?family=Noto+Serif:ital,wght@0,400;0,700;1,400&family=Open+Sans:wght@300;400;700&display=swap">
<style>
  :root {
    --stage: #333333;
    --screen: #f7f7f7;
    --panel: #ffffff;
    --line: #dcdcdc;
    --bar: #8a8a8a;
    --accent: #00c6f8;
    --brand: #8cc63f;
    --ink: #2b2b2b;
    --muted: #9a9a9a;
    --photo-a: #c9a46e;
    --photo-b: #7a5535;
  }
  * { box-sizing: border-box; margin: 0; padding: 0; }
  html, body { width: 1200px; height: 1000px; overflow: hidden; }
  body { background: var(--stage); position: relative; font-family: "Open Sans", sans-serif; color: var(--ink); }

  .screen { position: absolute; background: linear-gradient(180deg, var(--screen), #ffffff 60%, var(--screen)); overflow: hidden; }
  .screen--tablet { left: 156px; top: 215px; width: 430px; height: 582px; }
  .screen--phone { left: 753px; top: 262px; width: 325px; height: 484px; border: 1px solid #111; }

  .abs { position: absolute; }
  .brand { display: flex; align-items: center; gap: 4px; font-family: "Noto Serif", serif; color: var(--ink); }
  .brand__dot { width: 14px; height: 14px; border-radius: 50%; background: var(--brand); }
  .rule { height: 1px; background: var(--line); left: 0; right: 0; }

  .menu-bar { background: var(--bar); color: #fff; font-family: "Noto Serif", serif; font-weight: 700; font-size: 13px; display: flex; align-items: center; padding-left: 9px; }
  .search { background: #fff; border: 1px solid #c8c8c8; display: flex; align-items: center; gap: 6px; font-family: "Noto Serif", serif; font-style: italic; font-size: 10px; color: #555; padding: 0 6px; }
  .search svg { flex: none; }

  .hero { background: var(--panel); border: 1px solid #eaeaea; }
  .hero__photo { position: absolute; background: linear-gradient(160deg, #e8d8b8 0%, var(--photo-a) 35%, var(--photo-b) 75%, #5d4a3a 100%); }

  .tile { background: var(--panel); border: 1px solid #d4d4d4; display: flex; align-items: center; }
  .tile__icon { flex: none; width: 38px; height: 38px; background: var(--accent); display: flex; align-items: center; justify-content: center; margin-left: 10px; }
  .tile__text { flex: 1; padding-left: 13px; line-height: 1.15; }
  .tile__title { font-weight: 300; font-size: 20px; color: var(--ink); }
  .tile__sub { font-size: 11px; color: var(--muted); }
  .tile__count { flex: none; width: 34px; align-self: stretch; margin: 4px 0; border-left: 1px dotted #888; display: flex; align-items: center; justify-content: center; font-weight: 700; font-size: 18px; }

  .footer { font-family: "Noto Serif", serif; color: #777; display: flex; align-items: center; }
</style>
</head>
<body>

<!-- Tablet layout -->
<section class="screen screen--tablet" aria-label="Tablet home screen">
  <div class="abs brand" style="left:0;right:0;top:10px;justify-content:center;font-size:19px;">
    <span class="brand__dot"></span><span>brightlot</span>
  </div>

  <div class="abs menu-bar" style="left:11px;top:56px;width:406px;height:25px;">Menu</div>
  <div class="abs search" style="left:263px;top:60px;width:147px;height:18px;">
    <svg width="11" height="11" viewBox="0 0 12 12"><circle cx="5" cy="5" r="3.8" fill="none" stroke="#777" stroke-width="1.5"/><path d="M8 8l3 3" stroke="#777" stroke-width="1.6"/></svg>Search
  </div>

  <div class="abs hero" style="left:11px;top:90px;width:406px;height:222px;">
    <div class="hero__photo" role="img" aria-label="Photo of a bright open kitchen and dining room with wooden cabinets" style="left:6px;top:6px;width:394px;height:208px;"></div>
  </div>
  <div class="abs rule" style="top:322px;"></div>

  <div class="abs tile" style="left:17px;top:338px;width:394px;height:50px;">
    <span class="tile__icon"><svg width="18" height="20" viewBox="0 0 18 20"><path d="M9 1a6 6 0 0 0-6 6c0 5 6 12 6 12s6-7 6-12a6 6 0 0 0-6-6z" fill="#111"/><circle cx="9" cy="7" r="2.3" fill="#00c6f8"/></svg></span>
    <div class="tile__text"><div class="tile__title">Development projects</div><div class="tile__sub">Nova 12, Elm Park, Old Mill</div></div>
    <div class="tile__count">5</div>
  </div>
  <div class="abs tile" style="left:17px;top:397px;width:394px;height:50px;">
    <span class="tile__icon"><svg width="16" height="16" viewBox="0 0 16 16"><path d="M8 1l7 6v8H1V7z" fill="#111"/><circle cx="8" cy="10" r="2.2" fill="#00c6f8"/></svg></span>
    <div class="tile__text"><div class="tile__title">Space for rent</div><div class="tile__sub">Nova 12, Firehouse, factory</div></div>
    <div class="tile__count">9</div>
  </div>
  <div class="abs tile" style="left:17px;top:457px;width:394px;height:50px;">
    <span class="tile__icon"><svg width="16" height="16" viewBox="0 0 16 16"><path d="M6 1h4l4 13H2z" fill="#111"/><rect x="1" y="13" width="14" height="2" fill="#111"/><rect x="4" y="7" width="8" height="2" fill="#00c6f8"/></svg></span>
    <div class="tile__text"><div class="tile__title">Service</div><div class="tile__sub">Building Management, Real Estate Activity</div></div>
    <div class="tile__count">6</div>
  </div>

  <div class="abs rule" style="top:547px;"></div>
  <div class="abs footer" style="left:12px;right:0;top:556px;height:18px;font-size:10.5px;">
    <svg width="14" height="12" viewBox="0 0 14 12"><rect x="3" y="0" width="8" height="4" fill="#aaa"/><rect x="0" y="4" width="14" height="5" fill="#aaa"/><rect x="3" y="8" width="8" height="4" fill="#ccc"/></svg>
    <span style="margin-left:40px;">Copyright © 2013&nbsp; Brightlot Ltd. All rights reserved.</span>
  </div>
</section>

<!-- Phone layout -->
<section class="screen screen--phone" aria-label="Phone home screen">
  <div class="abs brand" style="left:11px;top:5px;font-size:15px;">
    <span class="brand__dot" style="width:12px;height:12px;"></span><span>brightlot</span>
  </div>
  <div class="abs rule" style="top:29px;"></div>
  <div class="abs search" style="left:11px;top:35px;width:300px;height:19px;justify-content:space-between;">
    <span>Search</span>
    <svg width="11" height="11" viewBox="0 0 12 12"><circle cx="5" cy="5" r="3.8" fill="none" stroke="#777" stroke-width="1.5"/><path d="M8 8l3 3" stroke="#777" stroke-width="1.6"/></svg>
  </div>
  <div class="abs menu-bar" style="left:11px;top:63px;width:300px;height:21px;font-size:12px;">Menu</div>
  <div class="abs rule" style="top:89px;"></div>

  <div class="abs hero" style="left:10px;top:99px;width:303px;height:163px;">
    <div class="hero__photo" role="img" aria-label="Photo of a bright open kitchen and dining room with wooden cabinets" style="left:5px;top:4px;width:292px;height:154px;"></div>
  </div>

  <div class="abs tile" style="left:10px;top:271px;width:303px;height:52px;">
    <span class="tile__icon" style="margin-left:4px;"><svg width="18" height="20" viewBox="0 0 18 20"><path d="M9 1a6 6 0 0 0-6 6c0 5 6 12 6 12s6-7 6-12a6 6 0 0 0-6-6z" fill="#111"/><circle cx="9" cy="7" r="2.3" fill="#00c6f8"/></svg></span>
    <div class="tile__text" style="padding-left:12px;"><div class="tile__title" style="font-size:19px;">Development projects</div><div class="tile__sub">Nova 12, Elm Park, Old Mill</div></div>
    <div class="tile__count">5</div>
  </div>
  <div class="abs tile" style="left:10px;top:327px;width:303px;height:52px;">
    <span class="tile__icon" style="margin-left:4px;"><svg width="16" height="16" viewBox="0 0 16 16"><path d="M8 1l7 6v8H1V7z" fill="#111"/><circle cx="8" cy="10" r="2.2" fill="#00c6f8"/></svg></span>
    <div class="tile__text" style="padding-left:12px;"><div class="tile__title" style="font-size:19px;">Space for rent</div><div class="tile__sub">Nova 12, Firehouse, factory</div></div>
    <div class="tile__count">9</div>
  </div>
  <div class="abs tile" style="left:10px;top:383px;width:303px;height:52px;">
    <span class="tile__icon" style="margin-left:8px;"><svg width="16" height="16" viewBox="0 0 16 16"><path d="M6 1h4l4 13H2z" fill="#111"/><rect x="1" y="13" width="14" height="2" fill="#111"/><rect x="4" y="7" width="8" height="2" fill="#00c6f8"/></svg></span>
    <div class="tile__text" style="padding-left:12px;"><div class="tile__title" style="font-size:19px;">Service</div><div class="tile__sub">Building Management, Real Estate</div></div>
    <div class="tile__count">6</div>
  </div>

  <div class="abs rule" style="top:463px;"></div>
  <div class="abs footer" style="left:4px;right:0;top:466px;height:14px;font-size:8.5px;">
    <svg width="12" height="11" viewBox="0 0 14 12"><rect x="3" y="0" width="8" height="4" fill="#aaa"/><rect x="0" y="4" width="14" height="5" fill="#aaa"/><rect x="3" y="8" width="8" height="4" fill="#ccc"/></svg>
    <span style="margin-left:46px;">Copyright © 2013&nbsp; Brightlot Ltd. All rights reserved.</span>
  </div>
</section>

</body>
</html>
```